Eastvale Physiotherapy Website www.eastvalephysiotherapy.com.au

Create Wordpress website for Eastvale Physiotherapy which aligns with our other locations www.marrowbankphysiotherapy,com.au. We would like the website to present in a similar fashion to our exisiting site with similar headings and layout. We will then alter the text to make it location specific.

Coding

Coded - Design and coding required

Number of Pages Required

1 page

Font styles to use
Sans Serif

Requirements
Must have
• Colours of the website must match the colours of the colour Eastvale Physiotherapy logo
• Website must be complimentary to existing websites,
• www.marrowbankphysiotherapy.com.au
• www.marrowbankpilatesandrehab.com.au

```html
<!DOCTYPE html>
<html lang="en">
<head>
<meta charset="utf-8">
<title>Eastvale Physiotherapy</title>
<link href="https://fonts.googleapis.com/css2?family=Raleway:wght@400;500;600;700&family=Open+Sans:wght@400;600;700&display=swap" rel="stylesheet">
<style>
:root{
  --navy:#2d2b63;
  --teal:#7cbfae;
  --ink:#222;
  --body:#555;
  --grey-band:#f1f1f1;
  --line:#cfcfcf;
  --footer:#2b2b2b;
  --footer-deep:#1d1d1d;
  --accent:#8cc63f;
  --send:#c9d400;
  --white:#fff;
}
*{box-sizing:border-box;margin:0;padding:0}
html,body{width:1200px;height:3136px;overflow:hidden;background:var(--white)}
body{position:relative;font-family:'Open Sans',sans-serif;color:var(--body)}
.abs{position:absolute}

/* header */
.site-header{left:0;top:0;width:1200px;height:118px;background:var(--white);z-index:3}
.brand{left:68px;top:38px;display:flex;align-items:center;gap:12px;font-family:'Raleway',sans-serif;font-weight:700;font-size:26px;color:var(--navy)}
.brand-dot{width:18px;height:18px;border-radius:50%;background:var(--navy)}
.topbar{right:70px;top:9px;display:flex;gap:26px;font-size:15px;color:#444;font-family:'Raleway',sans-serif}
.topbar span{display:flex;align-items:center;gap:6px}
.main-nav{right:70px;top:70px;display:flex;gap:40px;font-family:'Raleway',sans-serif;font-size:15px;font-weight:500;color:#333}
.main-nav a{color:inherit;text-decoration:none;padding-bottom:12px}
.main-nav a.active{border-bottom:3px solid var(--navy)}

/* hero */
.hero{left:0;top:118px;width:1200px;height:520px}
.hero-photo{position:absolute;inset:0;background:
  radial-gradient(ellipse 170px 210px at 790px 300px,rgba(214,170,145,.85),rgba(214,170,145,0) 100%),
  radial-gradient(ellipse 120px 90px at 900px 120px,rgba(200,150,120,.7),rgba(200,150,120,0) 100%),
  radial-gradient(ellipse 260px 300px at 960px 260px,rgba(95,98,104,.75),rgba(95,98,104,0) 100%),
  radial-gradient(ellipse 110px 170px at 760px 110px,rgba(190,80,70,.35),rgba(190,80,70,0) 100%),
  radial-gradient(ellipse 180px 120px at 1110px 430px,rgba(240,240,240,.9),rgba(240,240,240,0) 100%),
  linear-gradient(100deg,#e2e2e2 0%,#efefef 40%,#d6d3d1 70%,#e6e6e6 100%)}
.hero-curve{position:absolute;left:0;width:1200px}
.tagline-sm{left:68px;top:361px;background:rgba(95,95,95,.85);color:var(--white);font-family:'Raleway',sans-serif;font-size:28px;padding:2px 16px;letter-spacing:.5px}
.tagline-lg{left:68px;top:408px;background:rgba(60,60,60,.9);color:var(--white);font-family:'Raleway',sans-serif;font-weight:600;font-size:46px;padding:0 16px;letter-spacing:1px}

/* welcome */
.section-title{left:0;width:1200px;text-align:center;font-family:'Raleway',sans-serif;font-weight:400;font-size:34px;color:var(--ink);letter-spacing:.5px}
.rule{height:2px;background:#888;left:50%;transform:translateX(-50%)}
.welcome-text{left:95px;top:738px;width:1010px;text-align:center;font-size:14px;line-height:24.5px;color:#444}
.btn-outline{border:2px solid var(--navy);border-radius:6px;background:var(--white);color:#333;font-family:'Raleway',sans-serif;font-size:15px;text-align:center}
.book-btn{left:503px;top:960px;width:202px;height:48px;line-height:44px}
.note{left:0;top:1039px;width:1200px;text-align:center;font-size:18px;color:#444}
.note b{color:var(--navy);font-weight:600}

/* services */
.services-band{left:0;top:1090px;width:1200px;height:610px}
.service-grid{left:63px;top:1222px;width:1070px;height:470px;display:grid;grid-template-columns:repeat(3,1fr);grid-template-rows:repeat(2,1fr)}
.service{text-align:center;padding-top:12px}
.service:nth-child(-n+3){border-bottom:1px solid var(--line)}
.service:nth-child(3n+1),.service:nth-child(3n+2){border-right:1px solid var(--line)}
.service-icon{display:block;width:64px;height:64px;margin:0 auto 18px}
.service h3{font-family:'Raleway',sans-serif;font-weight:700;font-size:17px;color:#222;margin-bottom:6px}
.service p{font-size:14px;line-height:21px;color:#777;width:290px;margin:0 auto}

/* practitioners */
.practitioners-intro{left:80px;top:1786px;width:1040px;text-align:center;font-family:'Raleway',sans-serif;font-size:14.5px;line-height:22px;color:#555}
.team{left:60px;top:1942px;width:1080px;display:flex;justify-content:space-between}
.member{width:230px;text-align:center}
.portrait{width:192px;height:192px;margin:0 auto;border-radius:50%;border:5px solid #9a9a9a;background:radial-gradient(circle at 50% 40%,#e4e4e4,#a8a8a8)}
.member h4{margin-top:16px;font-family:'Open Sans',sans-serif;font-weight:700;font-size:14.5px;color:#222}
.member .role{font-size:14px;color:#555;margin-top:1px}
.member p{font-size:14px;line-height:21px;color:#666;margin-top:1px}
.member .read{display:inline-block;margin-top:10px;width:116px;height:36px;line-height:33px;border:1.5px solid #444;border-radius:3px;font-size:14px;color:#222}

/* map */
.map{left:0;top:2393px;width:1200px;height:418px;background:
  radial-gradient(ellipse 60px 240px at 830px 120px,rgba(170,215,235,.9),rgba(170,215,235,0) 100%),
  radial-gradient(ellipse 260px 40px at 1050px 210px,rgba(170,215,235,.85),rgba(170,215,235,0) 100%),
  radial-gradient(ellipse 200px 90px at 400px 300px,rgba(190,190,190,.7),rgba(190,190,190,0) 100%),
  radial-gradient(ellipse 300px 150px at 150px 150px,rgba(245,245,245,.9),rgba(245,245,245,0) 100%),
  linear-gradient(135deg,#e8e8e8,#dcdcdc 60%,#e4e8ea)}
.map-pin{left:482px;top:2520px}

/* footer */
.site-footer{left:0;top:2808px;width:1200px;height:275px;background:var(--footer);color:#ddd}
.footer-brand{left:68px;top:2944px;display:flex;align-items:center;gap:10px;font-family:'Raleway',sans-serif;font-weight:700;font-size:19px;color:#d8d8d8}
.footer-brand .brand-dot{background:#d8d8d8;width:14px;height:14px}
.footer-h{font-family:'Raleway',sans-serif;font-weight:400;font-size:22px;color:var(--white)}
.links{display:grid;grid-template-columns:110px 110px;column-gap:16px;row-gap:8px;font-size:14px;color:var(--white)}
.links span{border-bottom:1px solid #555;padding-bottom:8px}
.contact-phone{color:var(--accent);font-size:22px}
.contact-line{font-size:14px;color:var(--white);line-height:20px}
.socials{display:flex;gap:8px}
.socials i{width:20px;height:20px;border-radius:3px;background:#8a8a8a;display:block}
.newsletter-text{font-size:13px;line-height:20px;color:#ddd;width:260px}
.email{left:859px;top:2985px;width:215px;height:42px;background:var(--white);color:#aaa;font-size:13px;padding:12px 10px}
.send{left:1074px;top:2985px;width:42px;height:42px;background:var(--send);display:flex;align-items:center;justify-content:center}
.copyright{left:0;top:3083px;width:1200px;height:53px;background:var(--footer-deep);color:#ddd;text-align:center;line-height:53px;font-size:14px}
</style>
</head>
<body>

<header class="abs site-header">
  <div class="abs brand"><span class="brand-dot"></span>Eastvale Physiotherapy</div>
  <div class="abs topbar">
    <span><svg width="14" height="14" viewBox="0 0 14 14"><circle cx="7" cy="7" r="7" fill="#6bbf6b"/><path d="M7 3v8M3 7h8" stroke="#fff" stroke-width="2"/></svg>BOOK AN APPOINTMENT</span>
    <span><svg width="12" height="12" viewBox="0 0 24 24"><path d="M6 2l4 5-2 3a12 12 0 006 6l3-2 5 4-3 4C10 22 2 14 2 5z" fill="#777"/></svg>800-555-0142</span>
  </div>
  <nav class="abs main-nav">
    <a class="active">HOME</a><a>ABOUT</a><a>SERVICE</a><a>CONDITIONS</a><a>HEALTH TIPS</a><a>BLOG</a><a>CONTACT</a>
  </nav>
</header>

<section class="abs hero">
  <div class="hero-photo" role="img" aria-label="Physiotherapist treating a patient's neck in a clinic"></div>
  <svg class="hero-curve" style="top:0" height="40" viewBox="0 0 1200 40" preserveAspectRatio="none"><path d="M0 0H1200V0Q600 40 0 20Z" fill="#fff"/></svg>
  <svg class="hero-curve" style="bottom:0" height="60" viewBox="0 0 1200 60" preserveAspectRatio="none"><path d="M0 10Q600 80 1200 0V60H0Z" fill="#fff"/></svg>
</section>
<div class="abs tagline-sm">A PASSION FOR HEALING</div>
<div class="abs tagline-lg">MEDICAL CENTER</div>

<h1 class="abs section-title" style="top:676px">WELCOME TO EASTVALE PHYSIOTHERAPY</h1>
<div class="abs rule" style="top:724px;width:420px"></div>
<div class="abs welcome-text">
  <p>Eastvale Physiotherapy is an innovative physiotherapy practice offering comprehensive services by experienced and highly-qualified physiotherapists. We achieve outstanding clinical results for a broad range of common conditions including: back pain, neck pain, headache, migraine, shoulder pain, sports injuries, vertigo, knee pain, incontinence, persistent pelvic pain and women's health and men's health issues.</p>
  <p>Our team of physiotherapists have extensive experience from working in private practice, private and public hospitals, and research and teaching over a range of physiotherapy disciplines including sports, manipulative, musculoskeletal, neurological, pain management, continence, women's / men's health and paediatric services.</p>
  <p>We are confident our practice will offer a service that stands apart, as we value excellence in quality care delivered by highly-educated and experienced physiotherapists.</p>
</div>
<div class="abs btn-outline book-btn">BOOK ONLINE HERE*</div>
<p class="abs note">*Please note not all practitioners are available online – <b>please call xx xxx xx</b> to speak with our reception team.</p>

<section class="abs services-band">
  <svg width="1200" height="610" viewBox="0 0 1200 610" preserveAspectRatio="none"><path d="M0 30Q600 -30 1200 30V580Q600 640 0 580Z" fill="#f1f1f1"/></svg>
</section>
<h2 class="abs section-title" style="top:1140px">OUR SERVICES</h2>
<div class="abs rule" style="top:1186px;width:130px"></div>
<div class="abs service-grid">
  <div class="service">
    <svg class="service-icon" viewBox="0 0 64 64" role="img" aria-label="Stopwatch icon"><circle cx="30" cy="36" r="20" fill="none" stroke="#7cbfae" stroke-width="4"/><path d="M30 36V24M30 36l8 6" stroke="#7cbfae" stroke-width="4" stroke-linecap="round"/><rect x="25" y="8" width="10" height="6" rx="2" fill="#7cbfae"/></svg>
    <h3>PHYSIOTHERAPY</h3><p>Lorem Ipsum has been the industry's standard dummy text ever since the 1500s, when an unknown printer</p></div>
  <div class="service">
    <svg class="service-icon" viewBox="0 0 64 64" role="img" aria-label="Bed icon"><path d="M6 18v34M58 36v16M6 44h52M6 36h52" stroke="#7cbfae" stroke-width="4" stroke-linecap="round"/><rect x="10" y="26" width="12" height="8" rx="3" fill="#7cbfae"/><rect x="34" y="10" width="22" height="16" rx="2" fill="none" stroke="#7cbfae" stroke-width="3"/><path d="M37 19h4l2-4 3 8 2-4h5" stroke="#7cbfae" stroke-width="2" fill="none"/></svg>
    <h3>CHRONIC PAIN MANAGEMENT</h3><p>Lorem Ipsum has been the industry's standard dummy text ever since the 1500s, when an unknown printer</p></div>
  <div class="service">
    <svg class="service-icon" viewBox="0 0 64 64" role="img" aria-label="Clipboard icon"><rect x="14" y="12" width="36" height="46" rx="4" fill="none" stroke="#7cbfae" stroke-width="4"/><rect x="24" y="7" width="16" height="9" rx="2" fill="#7cbfae"/><path d="M32 26v16M24 34h16" stroke="#7cbfae" stroke-width="4"/></svg>
    <h3>KNEE CLINIC</h3><p>Lorem Ipsum has been the industry's standard dummy text ever since the 1500s, when an unknown printer</p></div>
  <div class="service">
    <svg class="service-icon" viewBox="0 0 64 64" role="img" aria-label="Medical screen icon"><path d="M6 16h52l-4 34H10z" fill="#7cbfae"/><path d="M32 24v18M23 33h18" stroke="#fff" stroke-width="5"/></svg>
    <h3>REAL TIME ULTRASOUND</h3><p>Lorem Ipsum has been the industry's standard dummy text ever since the 1500s, when an unknown printer</p></div>
  <div class="service">
    <svg class="service-icon" viewBox="0 0 64 64" role="img" aria-label="Treatment table icon"><rect x="4" y="34" width="56" height="6" rx="2" fill="#7cbfae"/><path d="M12 40v18M52 40v18" stroke="#7cbfae" stroke-width="4"/><rect x="8" y="26" width="40" height="8" rx="4" fill="#7cbfae"/></svg>
    <h3>WOMEN'S &amp; MEN'S HEALTH</h3><p>Lorem Ipsum has been the industry's standard dummy text ever since the 1500s, when an unknown printer</p></div>
  <div class="service">
    <svg class="service-icon" viewBox="0 0 64 64" role="img" aria-label="Heart icon"><path d="M32 54S8 40 8 24a12 12 0 0124-4 12 12 0 0124 4c0 16-24 30-24 30z" fill="none" stroke="#7cbfae" stroke-width="4"/><path d="M16 32h10l3-6 5 12 3-6h11" stroke="#7cbfae" stroke-width="3" fill="none"/></svg>
    <h3>OTHER SERVICES</h3><p>Lorem Ipsum has been the industry's standard dummy text ever since the 1500s, when an unknown printer</p></div>
</div>

<h2 class="abs section-title" style="top:1744px">OUR PRACTITIONERS</h2>
<p class="abs practitioners-intro">All practitioners at our clinic have completed or are completing postgraduate university training and most are involved in teaching, university lecturing and research. This means that you are being treated by highly qualified people at the forefront of new developments in the management of musculoskeletal disorders.</p>
<div class="abs rule" style="top:1870px;width:170px;background:#bbb"></div>
<div class="abs team">
  <div class="member"><div class="portrait" role="img" aria-label="Portrait of Clara Whitby"></div><h4>CLARA WHITBY</h4><div class="role">Director</div><p>Clara completed her Bachelor of physiotherapy at the University of Eastbrook in 2009 and more recently her Grade</p><span class="read">Read More</span></div>
  <div class="member"><div class="portrait" role="img" aria-label="Portrait of Dr Megan Hollis"></div><h4>DR MEGAN HOLLIS</h4><div class="role">Director</div><p>Clara completed her Bachelor of physiotherapy at the University of Eastbrook in 2009 and more recently her Grade</p><span class="read">Read More</span></div>
  <div class="member"><div class="portrait" role="img" aria-label="Portrait of Rachel Dunmore"></div><h4>RACHEL DUNMORE</h4><div class="role">Director</div><p>Clara completed her Bachelor of physiotherapy at the University of Eastbrook in 2009 and more recently her Grade</p><span class="read">Read More</span></div>
  <div class="member"><div class="portrait" role="img" aria-label="Portrait of Owen Halbrook"></div><h4>OWEN HALBROOK</h4><div class="role">B Pod M Physio</div><p>Clara completed her Bachelor of physiotherapy at the University of Eastbrook in 2009 and more recently her Grade</p><span class="read">Read More</span></div>
</div>

<div class="abs map" role="img" aria-label="Street map showing the clinic location"></div>
<svg class="abs map-pin" width="52" height="68" viewBox="0 0 52 68"><path d="M26 0C12 0 0 11 0 25c0 18 26 43 26 43s26-25 26-43C52 11 40 0 26 0z" fill="#1e9ad6"/><circle cx="26" cy="24" r="14" fill="#fff"/><path d="M26 16v16M18 24h16" stroke="#1e9ad6" stroke-width="4"/></svg>

<footer class="abs site-footer"></footer>
<div class="abs footer-brand"><span class="brand-dot"></span>Eastvale Physiotherapy</div>
<h5 class="abs footer-h" style="left:330px;top:2848px">Quick Links</h5>
<div class="abs links" style="left:330px;top:2898px">
  <span>Home</span><span>About</span><span>Alternative</span><span>News</span><span>Challenge</span><span>Contact</span><span>Shop</span>
</div>
<h5 class="abs footer-h" style="left:608px;top:2850px">Contact Us</h5>
<div class="abs contact-phone" style="left:608px;top:2900px">(888) XX XXX XX</div>
<div class="abs contact-line" style="left:610px;top:2936px">info@eastvalephysio.com.au</div>
<div class="abs contact-line" style="left:610px;top:2966px;display:flex;gap:6px">
  <svg width="14" height="20" viewBox="0 0 14 20"><path d="M7 0a7 7 0 00-7 7c0 5 7 13 7 13s7-8 7-13a7 7 0 00-7-7z" fill="#fff"/><circle cx="7" cy="7" r="2.5" fill="#2b2b2b"/></svg>
  <span>Harbourline Communications LLC<br>112 Riverside Ave #210</span>
</div>
<div class="abs socials" style="left:612px;top:3028px"><i></i><i></i><i></i><i></i><i></i></div>
<h5 class="abs footer-h" style="left:859px;top:2850px">Subscribe Newsletter</h5>
<p class="abs newsletter-text" style="left:859px;top:2902px">when an unknown printer took a galley of type and scrambled it to make a type specimen book.</p>
<div class="abs email">Email Address</div>
<div class="abs send"><svg width="20" height="18" viewBox="0 0 20 18"><path d="M0 8L20 0 14 18 10 11z" fill="#222"/></svg></div>
<div class="abs copyright">© Copyright 2018 practice website | All Rights Reserved</div>

</body>
</html>
```